QuellridgeStrategy Business Card Design

Design business cards with attached ideas. I am open to several different ideas that would be interesting and innovative. What I have provided is logo and colors. Font should be Helvetica although it could be bold or light as needed. The design can be vertical or horizontal. The design should be more interesting than a standard business card. Files must be ready to send to a printer and in Illustrator format. The text with the five icons should be exact. Send me some ideas and I will get back to you right away. I need to choose a design within 3-5 days.

Target Market(s)

Business audience

Industry/Entity Type

Business

Contact Information for Business Card

Files should be ready to send to printer in illustrator format

Font styles to use
Sans Serif

Colors
3276b5

Requirements
Must have
• Use attached logo and two colors - blue / gray
• Include 5 offering icons and text on back
Nice to have
• Interesting and innovative design. Vertical or horizontal are both fine.

```html
<!DOCTYPE html>
<html lang="en">
<head>
<meta charset="utf-8">
<title>QuellridgeStrategy Business Card</title>
<link href="https://fonts.googleapis.com/css2?family=Arimo:wght@400;700&display=swap" rel="stylesheet">
<style>
  :root {
    --blue: #3276b5;
    --blue-dark: #2a6399;
    --gray: #5b5d60;
    --ink: #3a3b3d;
    --paper: #f7f7f7;
    --stage: #e6e6e6;
  }
  * { box-sizing: border-box; margin: 0; padding: 0; }
  html, body { width: 1200px; height: 1023px; overflow: hidden; }
  body {
    background: var(--stage);
    font-family: "Arimo", "Helvetica Neue", Helvetica, Arial, sans-serif;
    position: relative;
  }
  .card {
    position: absolute;
    width: 620px;
    height: 354px;
    border-radius: 24px;
    background: var(--paper);
    overflow: hidden;
    box-shadow: 0 6px 18px rgba(0,0,0,0.18);
  }
  /* Front */
  .card-front { left: 80px; top: 80px; }
  .brand { position: absolute; left: 36px; top: 48px; display: flex; align-items: center; gap: 18px; }
  .brand-mark { width: 64px; height: 64px; background: var(--blue); border-radius: 6px; flex: none; }
  .brand-name { font-size: 36px; font-weight: 700; color: var(--blue); letter-spacing: -0.5px; line-height: 1; }
  .brand-tagline { font-size: 16px; color: var(--ink); margin-top: 6px; }
  .accent-column { position: absolute; left: 468px; top: 0; width: 96px; height: 150px; background: var(--gray); }
  .name-band { position: absolute; left: 0; top: 150px; width: 100%; height: 72px; background: var(--blue); padding: 14px 0 0 44px; color: #fff; }
  .person-name { font-size: 22px; font-weight: 700; }
  .person-title { font-size: 15px; margin-top: 3px; }
  .contacts { position: absolute; left: 44px; top: 240px; list-style: none; font-size: 15px; color: var(--ink); }
  .contacts li { display: flex; align-items: center; gap: 10px; height: 24px; }
  .contacts svg { width: 14px; height: 14px; fill: var(--blue); }
  .base-strip { position: absolute; left: 0; bottom: 0; width: 100%; height: 22px; background: var(--blue); }
  /* Back */
  .card-back { left: 500px; top: 590px; }
  .offerings-header { position: absolute; left: 0; top: 0; width: 66px; height: 100%; background: var(--blue); }
  .offerings-title {
    position: absolute; left: 33px; top: 177px;
    transform: translate(-50%, -50%) rotate(-90deg);
    white-space: nowrap; color: #fff; font-size: 22px; font-weight: 400;
  }
  .icon-column { position: absolute; left: 66px; top: 0; width: 72px; height: 100%; background: var(--gray); border-left: 4px solid #fff; }
  .offering-list { position: absolute; left: 138px; top: 0; list-style: none; }
  .offering {
    position: relative; height: 62px; display: flex; align-items: center;
    padding-left: 32px; font-size: 16px; color: var(--ink); white-space: nowrap;
  }
  .offering:first-child { margin-top: 22px; }
  .offering-icon {
    position: absolute; left: -66px; width: 56px; height: 56px; border-radius: 50%;
    background: var(--blue-dark); border: 4px solid #fff;
    display: flex; align-items: center; justify-content: center;
  }
  .offering-icon svg { width: 24px; height: 24px; fill: none; stroke: #fff; stroke-width: 2; }
  .offering-label { color: var(--blue); font-weight: 700; margin-right: 6px; }
</style>
</head>
<body>

<section class="card card-front">
  <div class="brand">
    <div class="brand-mark"></div>
    <div>
      <div class="brand-name">QuellridgeStrategy</div>
      <div class="brand-tagline">Clear Plans - Steady Results</div>
    </div>
  </div>
  <div class="accent-column"></div>
  <div class="name-band">
    <div class="person-name">Dana KELLER, PhD</div>
    <div class="person-title">Managing Director</div>
  </div>
  <ul class="contacts">
    <li><svg viewBox="0 0 16 16"><path d="M3 1h3l1 4-2 1a9 9 0 0 0 5 5l1-2 4 1v3a2 2 0 0 1-2 2A13 13 0 0 1 1 3a2 2 0 0 1 2-2z"/></svg>555-014-2287</li>
    <li><svg viewBox="0 0 16 16"><path d="M1 3h14v10H1z M1 3l7 6 7-6" stroke="#fff" stroke-width="1"/></svg>dana@quellridgestrategy.com</li>
    <li><svg viewBox="0 0 16 16"><circle cx="8" cy="8" r="7"/><path d="M1 8h14M8 1c-3 4-3 10 0 14M8 1c3 4 3 10 0 14" stroke="#fff" stroke-width="1" fill="none"/></svg>www.quellridgestrategy.com</li>
  </ul>
  <div class="base-strip"></div>
</section>

<section class="card card-back">
  <div class="offerings-header"><h2 class="offerings-title">Quellridge Strategy Offerings</h2></div>
  <div class="icon-column"></div>
  <ul class="offering-list">
    <li class="offering">
      <span class="offering-icon"><svg viewBox="0 0 24 24"><rect x="4" y="4" width="16" height="16"/><path d="M7 9h10M7 13h10M7 17h6"/></svg></span>
      <span class="offering-label">Concepts:</span>Thought leadership white papers
    </li>
    <li class="offering">
      <span class="offering-icon"><svg viewBox="0 0 24 24"><rect x="3" y="5" width="18" height="11"/><path d="M12 16v4M8 20h8"/></svg></span>
      <span class="offering-label">Curriculum:</span>Short courses on strategy
    </li>
    <li class="offering">
      <span class="offering-icon"><svg viewBox="0 0 24 24"><circle cx="7" cy="7" r="2.5"/><circle cx="17" cy="7" r="2.5"/><path d="M7 11v9M17 11v9"/></svg></span>
      <span class="offering-label">Coaching:</span>Building your strategic leadership
    </li>
    <li class="offering">
      <span class="offering-icon"><svg viewBox="0 0 24 24"><circle cx="12" cy="5" r="2.5"/><circle cx="5" cy="18" r="2.5"/><circle cx="19" cy="18" r="2.5"/><path d="M11 7l-5 9M13 7l5 9M7.5 18h9"/></svg></span>
      <span class="offering-label">Consulting:</span>Developing your strategic future
    </li>
    <li class="offering">
      <span class="offering-icon"><svg viewBox="0 0 24 24"><path d="M4 20h16M6 20v-6M11 20V9M16 20v-9"/><path d="M5 10l6-5 4 3 5-4"/></svg></span>
      <span class="offering-label">ScoreCard:</span>Balanced ScoreCard and software
    </li>
  </ul>
</section>

</body>
</html>
```